Presentation Folder Saguaro Plan Advisors

I would like a two sided presentation folder 9" wide x 12" tall for our benefits/ insurance company. It must be professional and instill confidence in our customers. ArtHive designed our logo which must be included. Our website is www.spallc-example.org The logo on the website is the old one as a new website is about to launch. The contact information and address are correct on the website. We provide health, disability and other benefits to employers and will use this when making presentations about plans and renewals. I have been told to put this as stationery from someone at ArtHive but it is not stationery. Please feel free to email me if you have questions.

Reason: My committee meets Oct. 17.

```html
<!DOCTYPE html>
<html lang="en">
<head>
<meta charset="utf-8">
<title>Saguaro Plan Advisors – Presentation Folder Inside Spread</title>
<link rel="stylesheet" href="https://fonts.googleapis.com/css2?family=Cinzel:wght@400;500&family=Lato:wght@300;400&display=swap">
<style>
  :root {
    --backdrop: #dcdcdd;
    --paper: #ffffff;
    --paper-shade: #f1f1f2;
    --navy: #262672;
    --navy-deep: #1d1d5c;
    --gold: #bf8a2b;
    --steel: #9b9fa1;
    --steel-light: #c4c6c8;
    --ink: #3a3a44;
    --rule: #c9c9cc;
  }
  * { margin: 0; padding: 0; box-sizing: border-box; }
  html, body {
    width: 1200px;
    height: 1200px;
    overflow: hidden;
    background: var(--backdrop);
  }
  .canvas {
    position: relative;
    width: 1200px;
    height: 1200px;
  }
  .folder-spread {
    position: absolute;
    left: 60px;
    top: 240px;
    width: 1080px;
    height: 720px;
    filter: drop-shadow(0 12px 22px rgba(0,0,0,0.16));
  }
  .brand-name {
    font-family: "Cinzel", serif;
    font-weight: 500;
    fill: var(--navy);
  }
  .brand-tagline {
    font-family: "Lato", sans-serif;
    font-weight: 400;
    fill: var(--gold);
    letter-spacing: 0.6px;
  }
  .card-name {
    font-family: "Lato", sans-serif;
    font-weight: 400;
    fill: var(--navy);
  }
  .card-title {
    font-family: "Lato", sans-serif;
    font-weight: 400;
    fill: var(--gold);
  }
  .card-detail {
    font-family: "Lato", sans-serif;
    font-weight: 300;
    fill: var(--ink);
  }
  .die-line {
    fill: none;
    stroke: var(--rule);
    stroke-width: 0.8;
    stroke-dasharray: 3 3;
  }
</style>
</head>
<body>
<main class="canvas">
  <svg class="folder-spread" viewBox="0 0 1080 720" xmlns="http://www.w3.org/2000/svg" aria-label="Saguaro Plan Advisors presentation folder, inside spread">
    <defs>
      <linearGradient id="steel-band" x1="0" y1="0" x2="1" y2="0">
        <stop offset="0" stop-color="var(--steel-light)"/>
        <stop offset="1" stop-color="var(--steel)"/>
      </linearGradient>
      <linearGradient id="navy-band" x1="0" y1="0" x2="1" y2="0">
        <stop offset="0" stop-color="var(--navy-deep)"/>
        <stop offset="1" stop-color="var(--navy)"/>
      </linearGradient>
      <clipPath id="left-pocket-clip">
        <path d="M0,620 L70,565 L470,548 L530,630 L540,720 L0,720 Z"/>
      </clipPath>
      <clipPath id="right-pocket-clip">
        <path d="M540,720 L550,630 L610,548 L1010,565 L1080,620 L1080,720 Z"/>
      </clipPath>
    </defs>

    <!-- Panels -->
    <g class="panel panel-left">
      <rect x="0" y="0" width="540" height="720" fill="var(--paper)"/>
      <polygon class="pocket-back-tab" points="0,450 185,515 185,620 0,620" fill="var(--steel)"/>
    </g>
    <g class="panel panel-right">
      <rect x="540" y="0" width="540" height="720" fill="var(--paper)"/>
      <polygon class="pocket-back-tab" points="895,515 1080,450 1080,620 895,620" fill="var(--navy)"/>
    </g>
    <line class="spine" x1="540" y1="0" x2="540" y2="720" stroke="var(--rule)" stroke-width="1"/>

    <!-- Left pocket -->
    <g class="pocket pocket-left">
      <path d="M0,620 L70,565 L470,548 L530,630 L540,720 L0,720 Z" fill="var(--paper-shade)"/>
      <g clip-path="url(#left-pocket-clip)">
        <path d="M0,540 L540,540 L540,600 Q300,615 0,650 Z" fill="url(#steel-band)"/>
        <path d="M0,650 Q300,615 540,600 L540,610 Q300,625 0,660 Z" fill="var(--gold)"/>
        <path d="M330,620 Q440,606 540,600 L540,700 L430,700 Z" fill="var(--gold)" role="img" aria-label="Gold geometric lattice pattern"/>
      </g>
      <path class="die-line" d="M70,565 L40,620 M470,548 L500,620"/>
    </g>

    <!-- Business card -->
    <g class="business-card">
      <path d="M110,575 L340,562 L340,640 L350,652 L350,700 L115,712 Z" fill="var(--paper)" stroke="var(--rule)" stroke-width="0.8"/>
      <rect x="130" y="593" width="9" height="9" fill="var(--navy)"/>
      <text class="brand-name" x="145" y="602" font-size="10">Saguaro Plan Advisors</text>
      <text class="brand-tagline" x="145" y="611" font-size="5">Employee Benefit Solutions</text>
      <text class="card-name" x="130" y="638" font-size="10">Your Name</text>
      <text class="card-title" x="130" y="649" font-size="7">Position</text>
      <text class="card-detail" x="225" y="640" font-size="5.5">1200 E. Camelback Rd, Suite 300</text>
      <text class="card-detail" x="225" y="648" font-size="5.5">Phoenix, AZ 85016</text>
      <text class="card-detail" x="225" y="664" font-size="5.5">Toll free: 800-555-0150</text>
      <text class="card-detail" x="225" y="672" font-size="5.5">Local: 602-555-0148</text>
      <text class="card-detail" x="225" y="680" font-size="5.5">Email: info@spallc-example.org</text>
    </g>

    <!-- Right pocket -->
    <g class="pocket pocket-right">
      <path d="M540,720 L550,630 L610,548 L1010,565 L1080,620 L1080,720 Z" fill="var(--paper-shade)"/>
      <g clip-path="url(#right-pocket-clip)">
        <path d="M540,540 L1080,540 L1080,650 Q800,600 540,605 Z" fill="url(#navy-band)"/>
        <path d="M540,605 Q800,600 1080,650 L1080,662 Q800,612 540,617 Z" fill="var(--gold)"/>
        <path d="M540,617 Q610,612 700,612 L620,700 L540,700 Z" fill="var(--gold)" role="img" aria-label="Gold geometric lattice pattern"/>
      </g>
      <path class="die-line" d="M1010,565 L1040,620"/>
      <g class="pocket-brand">
        <rect x="838" y="645" width="14" height="14" fill="var(--navy)"/>
        <text class="brand-name" x="860" y="658" font-size="15">Saguaro Plan Advisors</text>
        <text class="brand-tagline" x="860" y="670" font-size="6.5">Employee Benefit Solutions</text>
      </g>
    </g>
  </svg>
</main>
</body>
</html>
```